Email footer project

We are looking for a standardised email footer that can be changed monthly for various project we are working on.
Please refer to EMAIL FOOTER BRIEF FOR ALL INFORMATION

We have uploaded some previous footers as a sample.

Target Market(s)

property, environmental

Industry/Entity Type

energy and property

Colors
00AB8E
00BBA5
67D7C9
C6EFE9
E9F9F6

Requirements
Must have
• company branding - leafmarker.co.uk.

```html
<!DOCTYPE html>
<html lang="en">
<head>
<meta charset="utf-8">
<title>EPC Legislation Online Event – Footer Banner</title>
<link rel="stylesheet" href="https://fonts.googleapis.com/css2?family=Montserrat:wght@400;700;800&display=swap">
<style>
  :root {
    --page-bg: #d3d8dc;
    --green-dark: #2a7a3d;
    --green-mid: #2f9440;
    --green-bright: #39b54a;
    --photo-grey: #9aa4ad;
    --photo-light: #c4cbd1;
    --photo-suit: #4f5966;
    --white: #ffffff;
  }
  * { margin: 0; padding: 0; box-sizing: border-box; }
  html, body {
    width: 1200px;
    height: 355px;
    overflow: hidden;
    background: var(--page-bg);
    font-family: "Montserrat", Arial, sans-serif;
  }
  .footer-banner {
    position: absolute;
    left: 0;
    top: 81px;
    width: 1200px;
    height: 192px;
    background: linear-gradient(90deg, var(--green-dark) 0%, var(--green-mid) 45%, var(--green-bright) 88%);
    color: var(--white);
    overflow: hidden;
  }
  .headline {
    position: absolute;
    left: 48px;
    top: 36px;
    font-size: 35px;
    line-height: 42px;
    font-weight: 400;
    letter-spacing: 0.2px;
    text-transform: uppercase;
    white-space: nowrap;
  }
  .headline strong { font-weight: 700; }
  .event-cta {
    position: absolute;
    left: 609px;
    top: 56px;
    width: 254px;
    text-align: center;
  }
  .event-label {
    display: block;
    font-size: 25px;
    font-weight: 400;
    letter-spacing: 0.6px;
    line-height: 30px;
    margin-bottom: 4px;
  }
  .register-button {
    display: block;
    height: 43px;
    border: 2px solid var(--white);
    border-radius: 22px;
    font-size: 23px;
    font-weight: 800;
    letter-spacing: 1px;
    line-height: 39px;
    color: var(--white);
    text-decoration: none;
  }
  .energy-photo {
    position: absolute;
    right: 0;
    top: 0;
    width: 300px;
    height: 192px;
    background:
      radial-gradient(ellipse 90px 110px at 150px 120px, rgba(79, 89, 102, 0.55), rgba(79, 89, 102, 0) 100%),
      linear-gradient(90deg, rgba(57, 181, 74, 1) 0%, rgba(57, 181, 74, 0) 22%),
      linear-gradient(90deg, var(--photo-suit) 20%, var(--photo-grey) 65%, var(--photo-light) 100%);
  }
</style>
</head>
<body>
  <section class="footer-banner">
    <h1 class="headline">
      Are you reading for<br>
      <strong>EPC legislation</strong> changes<br>
      in April 2023?
    </h1>

    <div class="event-cta">
      <span class="event-label">ONLINE EVENT</span>
      <a class="register-button" href="#">REGISTER HERE</a>
    </div>

    <div class="energy-photo" role="img" aria-label="Photo of a businessman pointing at a glowing house outline containing an A to G energy efficiency rating chart"></div>
  </section>
</body>
</html>
```